KTR Builders
Home Page
Project: KTR Builders
KTR Builders  -
Creative Brief
www.ktrbuilders.com
KTR Builders is a residential general contractor. We build new custom homes, house additions, bathroom and kitchen remodeling.
We also can do medium size commercial buildings and office space buildout.
KTR Builders is also trained installer of the Brindell Pools.
We Need template of the home page and design of the sub pages.
yellow
Verdana, Trebuchet MS, Georgia

```html
<!DOCTYPE html>
<html lang="en">
<head>
<meta charset="utf-8">
<title>KTR Builders – Home</title>
<link rel="stylesheet" href="https://fonts.googleapis.com/css2?family=Open+Sans:wght@300;400;600;700&family=PT+Sans:wght@400&display=swap">
<style>
  :root {
    --canvas: #eceef1;
    --panel: #ffffff;
    --ink: #5a5f66;
    --ink-soft: #8a9097;
    --brand-gray: #6b7078;
    --accent: #2b84c8;
    --band: rgba(12, 14, 18, 0.88);
    --band-text: #c9ccd0;
    --rule: #e3e6ea;
    --frame: #d9dde2;
  }
  * { margin: 0; padding: 0; box-sizing: border-box; }
  html, body { width: 1200px; height: 833px; overflow: hidden; }
  body {
    position: relative;
    background: linear-gradient(180deg, #f7f8fa 0%, var(--canvas) 55%, #e4e7eb 100%);
    font-family: "PT Sans", Verdana, sans-serif;
    color: var(--ink);
  }
  .page {
    position: absolute; left: 199px; top: 0; width: 809px; height: 780px;
    background: var(--panel);
    box-shadow: 0 0 18px rgba(0,0,0,0.06);
  }
  .brand {
    position: absolute; left: 24px; top: 28px;
    display: flex; align-items: center; gap: 12px;
  }
  .brand-mark { width: 40px; height: 40px; background: var(--accent); }
  .brand-name {
    font-family: "Open Sans", sans-serif; font-weight: 700;
    font-size: 28px; letter-spacing: 0.5px; color: var(--brand-gray);
    white-space: nowrap;
  }
  .main-nav {
    position: absolute; left: 24px; top: 102px; right: 24px; height: 30px;
    border-bottom: 1px solid var(--rule);
    display: flex; align-items: center;
  }
  .main-nav a {
    font-family: "Open Sans", sans-serif; font-size: 10px;
    color: var(--ink-soft); text-decoration: none; margin-right: 20px;
  }
  .main-nav a.current { color: #2c3036; font-weight: 600; }
  .search-box {
    position: absolute; right: 12px; top: 6px; width: 180px; height: 18px;
    border: 1px solid var(--frame); background: #fafbfc;
  }
  .hero {
    position: absolute; left: 24px; top: 139px; width: 754px; height: 305px;
    overflow: hidden;
  }
  .hero-photo {
    position: absolute; inset: 0;
    background:
      linear-gradient(105deg, rgba(255,255,255,0) 45%, rgba(70,90,110,0.55) 46%, rgba(40,60,85,0.75) 80%, rgba(150,170,185,0.6) 100%),
      linear-gradient(180deg, #cfe3f2 0%, #9cc3e0 50%, #6e93b3 100%);
  }
  .hero-quote {
    position: absolute; left: 0; top: 176px; width: 476px; height: 94px;
    background: var(--band); padding: 8px 16px 0 14px;
    font-family: "Open Sans", sans-serif; text-transform: uppercase;
    white-space: nowrap;
  }
  .hero-quote .lead { font-weight: 300; font-size: 17px; color: var(--band-text); line-height: 22px; }
  .hero-quote .strong { font-weight: 400; font-size: 23px; color: #fff; line-height: 30px; }
  .hero-quote .tail { font-weight: 300; font-size: 17px; color: var(--band-text); line-height: 22px; text-align: right; }
  .section-title {
    position: absolute;
    font-family: "Open Sans", sans-serif; font-weight: 300;
    font-size: 27px; color: var(--accent); text-transform: uppercase;
    white-space: nowrap;
  }
  .welcome-title { left: 34px; top: 478px; }
  .showcase-title { left: 516px; top: 478px; }
  .welcome-intro {
    position: absolute; left: 34px; top: 516px; width: 456px;
    font-size: 10px; line-height: 13px; color: var(--ink);
  }
  .welcome-photo {
    position: absolute; left: 34px; top: 590px; width: 192px; height: 150px;
    border: 5px solid #eef0f3; outline: 1px solid var(--frame);
    background: linear-gradient(180deg, #b9d3ea 0%, #dfe6ec 45%, #a9b0b7 70%, #6f7a72 100%);
  }
  .welcome-body {
    position: absolute; left: 234px; top: 588px; width: 256px;
    font-size: 10px; line-height: 13px; color: var(--ink);
  }
  .showcase-grid {
    position: absolute; left: 516px; top: 515px;
    display: grid; grid-template-columns: repeat(3, 80px); grid-auto-rows: 72px;
    column-gap: 14px; row-gap: 13px;
  }
  .showcase-item { background: linear-gradient(160deg, #d7e9f7 0%, #6fa3cf 55%, #3c6f9e 100%); }
  .showcase-item.alt { background: linear-gradient(200deg, #e4edf3 0%, #9fb6c9 50%, #5e7c98 100%); }
  .showcase-item.warm { background: linear-gradient(170deg, #cfe2ee 0%, #a4b8a0 60%, #6f8a6a 100%); }
  .site-footer {
    position: absolute; left: 199px; top: 801px; width: 809px; text-align: center;
    font-size: 10px; color: var(--ink-soft);
  }
</style>
</head>
<body>
  <div class="page">
    <header class="brand">
      <span class="brand-mark"></span>
      <span class="brand-name">KTR BUILDERS INC.</span>
    </header>

    <nav class="main-nav">
      <a class="current" href="#">Home</a>
      <a href="#">About</a>
      <a href="#">Services</a>
      <a href="#">Products</a>
      <a href="#">Partners</a>
      <a href="#">Contacts</a>
      <span class="search-box"></span>
    </nav>

    <section class="hero">
      <div class="hero-photo" role="img" aria-label="Modern glass office building against a bright blue sky"></div>
      <div class="hero-quote">
        <p class="lead">We are what we repeatedly do</p>
        <p class="strong">Excellence, therefore, is not an</p>
        <p class="tail">act, but a habit</p>
      </div>
    </section>

    <h1 class="section-title welcome-title">Welcome to our site</h1>
    <p class="welcome-intro">We build custom homes, house additions and remodeled kitchens and bathrooms with care. Our crews plan every detail, keep each site clean and finish on schedule. We also deliver medium commercial buildings and office buildouts, and we handle every permit, inspection and final cleanup for owners who want a calm build.</p>
    <div class="welcome-photo" role="img" aria-label="Two-storey commercial building with a paved drive"></div>
    <p class="welcome-body">Every project starts with a clear plan, an honest estimate and a schedule you can trust. From the first sketch to the final walk through, one project manager stays with you and answers every question. We work with local suppliers, licensed trades and proven materials so each home stands strong for decades. Whether you need a new kitchen, a second story or a complete custom home, our team is ready to help you build it right.</p>

    <h2 class="section-title showcase-title">Our showcase</h2>
    <div class="showcase-grid">
      <div class="showcase-item" role="img" aria-label="Glass tower facade"></div>
      <div class="showcase-item alt" role="img" aria-label="Curved office building"></div>
      <div class="showcase-item" role="img" aria-label="High-rise seen from below"></div>
      <div class="showcase-item warm" role="img" aria-label="Office block with trees"></div>
      <div class="showcase-item alt" role="img" aria-label="Modern building corner"></div>
      <div class="showcase-item" role="img" aria-label="Blue glass facade"></div>
      <div class="showcase-item" role="img" aria-label="Tower against clear sky"></div>
      <div class="showcase-item alt" role="img" aria-label="Rounded glass building"></div>
      <div class="showcase-item" role="img" aria-label="Mirrored glass tower"></div>
    </div>
  </div>

  <footer class="site-footer">Copyright © 2011 KTRBuilders.com. All Rights Reserved.</footer>
</body>
</html>
```